Business card design needed for elearning/LMS consultant

I'm an elearning and learning management system (LMS) consultant that requires a minimalist, technology/cutting edge, business card. I do not have a logo or colour scheme. I offer clients hands on expertise in 'elearning authouring', 'LMS ecosystems', 'elearning strategy', 'technical implementation', 'mlearning', 'LMS evaluation', 'big data', 'learner analytics' and 'reporting strategy', 'social learning', 'elearning blueprint'. I'm thinking a 'tag cloud' of the above services on the back of the card, with contact details on front, but unsure if it's passe so please don't let it constrain you.

Target Market(s)

C-level executives, learning and development senior management,

Industry/Entity Type

Business

Contact Information for Business Card

Dorian Vastwick
dorian.vastwick@mailbrook.net
0417 362 958

Requirements
Should not have
• cheesy headshots, overused stockphotos, CLIPART and comic sans ;)

```html
<!DOCTYPE html>
<html lang="en">
<head>
<meta charset="utf-8">
<title>Dorian Vastwick — Business Card</title>
<link rel="stylesheet" href="https://fonts.googleapis.com/css2?family=Jost:wght@600;700&display=swap">
<style>
  :root {
    --stage: #2e2f31;
    --card-white: #ffffff;
    --teal: #00b0bf;
    --teal-deep: #1c9498;
    --orange: #e8922a;
    --grey-tile: #b8b9bb;
    --ice: #e6fcfc;
    --ink-light: #ffffff;
  }
  html, body {
    margin: 0;
    padding: 0;
    width: 1200px;
    height: 1139px;
    overflow: hidden;
    background: var(--stage);
  }
  .canvas {
    position: relative;
    width: 1200px;
    height: 1139px;
  }
  .card {
    position: absolute;
    width: 750px;
    height: 428px;
    display: block;
    font-family: "Jost", "Futura", sans-serif;
  }
  .card--front { left: 123px; top: 73px; }
  .card--back  { left: 358px; top: 574px; }
  .card-name { font-weight: 700; font-size: 56px; fill: var(--teal); letter-spacing: -1px; }
  .card-name .initial { fill: var(--orange); }
  .contact-heading { font-weight: 700; font-size: 62px; fill: var(--orange); letter-spacing: -1px; }
  .contact-line { font-weight: 600; font-size: 30px; fill: var(--ink-light); }
  .contact-phone { font-size: 34px; }
</style>
</head>
<body>
<main class="canvas">

  <svg class="card card--front" viewBox="0 0 824 470" aria-label="Card front">
    <defs>
      <clipPath id="front-shape"><rect width="824" height="470" rx="22"/></clipPath>
      <linearGradient id="front-tiles" x1="0" y1="0" x2="1" y2="0">
        <stop offset="0" stop-color="#b8b9bb"/>
        <stop offset="0.55" stop-color="#d2d3d4"/>
        <stop offset="1" stop-color="#ffffff"/>
      </linearGradient>
    </defs>
    <g clip-path="url(#front-shape)">
      <rect class="card-base" width="824" height="470" fill="var(--card-white)"/>
      <polygon class="tile-field" role="img" aria-label="Diagonal field of grey square pixel tiles with one orange tile"
               points="0,0 824,0 824,60 0,420" fill="url(#front-tiles)"/>
      <line class="accent-stripe" x1="100" y1="478" x2="830" y2="198" stroke="var(--orange)" stroke-width="5"/>
      <polygon class="teal-band" points="122,470 830,205 830,470" fill="var(--teal)"/>
      <text class="card-name" transform="translate(282 402) rotate(-21)">
        <tspan class="initial">D</tspan>ORIAN <tspan class="initial">V</tspan>ASTWICK
      </text>
    </g>
  </svg>

  <svg class="card card--back" viewBox="0 0 824 470" aria-label="Card back">
    <defs>
      <clipPath id="back-shape"><rect width="824" height="470" rx="22"/></clipPath>
      <linearGradient id="back-tiles" x1="0" y1="0" x2="1" y2="0">
        <stop offset="0" stop-color="#1c9498"/>
        <stop offset="0.6" stop-color="#12a3ad"/>
        <stop offset="1" stop-color="#00b0bf"/>
      </linearGradient>
    </defs>
    <g clip-path="url(#back-shape)">
      <rect class="card-base" width="824" height="470" fill="var(--teal)"/>
      <polygon class="tile-field" role="img" aria-label="Diagonal field of darker teal square pixel tiles"
               points="0,0 824,0 824,60 0,430" fill="url(#back-tiles)"/>
      <line class="accent-stripe" x1="80" y1="478" x2="830" y2="186" stroke="var(--orange)" stroke-width="5"/>
      <polygon class="ice-band" points="102,470 830,194 830,470" fill="var(--ice)"/>

      <g class="contact-email" transform="translate(262 320) rotate(-21)">
        <g class="icon-mail" fill="none" stroke="var(--ink-light)" stroke-width="2.2">
          <rect x="0" y="-24" width="36" height="24" rx="2"/>
          <polyline points="0,-24 18,-10 36,-24"/>
        </g>
        <text class="contact-line" x="48" y="0">dorian.vastwick@mailbrook.net</text>
      </g>

      <g class="contact-phone-row" transform="translate(285 362) rotate(-21)">
        <path class="icon-phone" fill="none" stroke="var(--ink-light)" stroke-width="2.4" stroke-linecap="round"
              d="M6,-26 l6,-2 l5,9 l-4,4 q4,8 12,12 l4,-4 l9,5 l-2,6 q-4,4 -10,2 q-16,-6 -22,-22 q-2,-6 2,-10z"/>
        <text class="contact-line contact-phone" x="48" y="0">0417 362 958</text>
      </g>

      <text class="contact-heading" transform="translate(312 432) rotate(-21)">CONTACT</text>
    </g>
  </svg>

</main>
</body>
</html>
```